Mind-Body Counsellor Needs a Flyer

Please refer to the attachment for the content of the flyer.

I need a 99x210mm double sided leaflet design for my Vancouver BC based counselling practice.

I am a somatic counsellor who helps people with chronic body symptoms transform their experiences by working on the emotional, historical and relational aspects of the body difficulty. I use art, movement and body awareness in my practice to support and follow my client's unique process. I believe in the power and creativity of the body symptoms itself to show a needed direction. My clients report that this process is transformational, and helps change the relationship they have with their symptom. Often the symptom itself is relieved as the person integrates the needed changes in their life. People say they feel more alive, whole and aware of their overall path in life through this process. I am trained in Flowfield Awareness Method.

I will be bringing the flyer to Doctors and Massage Therapists offices to get new referrals of clients who seek pain management with no relief in the conventional medical system. I would like designs that show diversity of cultures and body types. The final design should communicate professionalism, creativity, hope and healing.

Target Market(s)

Physician and health practitioners who can refer clients with difficulties relating to anxiety, depression, and medically untreatable body symptoms

Industry/Entity Type

Counsellor

Font styles to use
Sans Serif

Colors
ffcf3e
ffc214
fbee3d
cadf82
acd037
9bcb3c

Requirements
Must have
• Visual impact
• A sense of hope and transformation
• Sense of professionalism and creativity
Nice to have
• May or may not include people - but if it does, must represent diverse genders, ages, races, abilities etc.
Should not have
• Too text heavy
• For some reason the uploader is not working - I'll get the text uploaded by tomorrow!

```html
<!DOCTYPE html>
<html lang="en">
<head>
<meta charset="utf-8">
<title>Maren Holloway – Counselling Flyer</title>
<link href="https://fonts.googleapis.com/css2?family=Source+Sans+3:wght@300;400;600;700&family=Caveat:wght@500&display=swap" rel="stylesheet">
<style>
  :root{
    --backdrop:#7a4f2d;
    --blue-deep:#2f7cc9;
    --blue-light:#5b9fd8;
    --blue-wave:#4a90d0;
    --green:#9ecb3c;
    --green-pill:#a9d038;
    --green-pale:#cde38a;
    --yellow:#f6ef3e;
    --navy:#243a8c;
    --heading-blue:#1f4199;
    --white:#ffffff;
    --ink:#1d1d1d;
  }
  *{box-sizing:border-box;margin:0;padding:0}
  html,body{width:1200px;height:1178px;overflow:hidden}
  body{background:var(--backdrop);font-family:"Source Sans 3",sans-serif;position:relative}
  .side{position:absolute;overflow:hidden;box-shadow:4px 5px 8px rgba(0,0,0,.45)}

  /* front */
  .front{left:110px;top:102px;width:970px;height:458px;
    background:linear-gradient(100deg,var(--blue-deep) 30%,var(--blue-light) 100%)}
  .hero-photo{position:absolute;left:0;top:0;width:400px;height:458px;
    background:linear-gradient(160deg,#7fb6e4 0%,#d9e9f5 100%);
    -webkit-mask-image:linear-gradient(90deg,#000 80%,transparent 100%);
            mask-image:linear-gradient(90deg,#000 80%,transparent 100%)}
  .front .call{position:absolute;left:43px;top:394px;font-size:32px;color:var(--navy);white-space:nowrap}
  .call strong{font-weight:700}
  .identity{position:absolute;left:356px;top:24px;color:var(--white)}
  .identity .name{font-size:29px;font-weight:400;line-height:1.1}
  .identity .creds{font-size:19px;line-height:1.2}
  .motto{position:absolute;left:338px;top:96px;width:590px;height:40px;border-radius:20px;
    background:var(--green-pill);color:var(--white);font-size:30px;line-height:40px;padding-left:19px}
  .about{position:absolute;left:356px;top:156px;width:573px;color:var(--white);font-size:14.4px;font-weight:300;line-height:19.6px;text-align:justify}
  .about p+p{margin-top:10px}
  .session-photo{position:absolute;left:355px;top:298px;width:279px;height:144px;border:2px solid var(--white);border-radius:8px;
    background:linear-gradient(135deg,#e9e6e2,#c9c0b6 50%,#efece8);box-shadow:0 2px 4px rgba(0,0,0,.3)}
  .info-box{position:absolute;background:var(--yellow);border:2px solid var(--white);border-radius:9px;box-shadow:0 2px 4px rgba(0,0,0,.3)}
  .info-box h3{color:var(--heading-blue);font-weight:700}
  .info-box ul{list-style:none}
  .info-box li{position:relative;color:var(--ink)}
  .info-box li::before{content:"";position:absolute;left:0;border-radius:50%;
    background:radial-gradient(circle at 40% 40%,#9cc4ee 0,#3f78c8 55%,#1f4a9a 100%);border:1px solid #c6d9ee}
  .qualifications{left:650px;top:298px;width:280px;height:146px;padding:5px 8px}
  .qualifications h3{font-size:17px;margin-bottom:4px}
  .qualifications li{font-size:14.4px;line-height:18px;padding-left:24px;margin-bottom:4px}
  .qualifications li::before{top:2px;width:14px;height:14px}

  /* back */
  .back{left:115px;top:602px;width:969px;height:456px;background:var(--green)}
  .back .wave{position:absolute;left:0;top:0}
  .testimonials{position:absolute;left:38px;top:22px;width:365px;color:var(--white)}
  .testimonials h2{font-family:"Caveat",cursive;font-weight:500;font-size:41px;line-height:1.1;color:#1b1b1b;margin-bottom:12px;white-space:nowrap}
  .quote{font-size:14.4px;line-height:21px;text-align:justify;font-weight:300}
  .quote cite{display:block;font-style:normal;font-weight:400;text-align:left}
  .quote+.quote{margin-top:24px}
  .suited{left:460px;top:34px;width:460px;height:204px;padding:10px 10px}
  .suited h3{font-size:21px;margin-bottom:10px}
  .suited li{font-size:18px;line-height:22px;padding-left:30px;margin-bottom:7px}
  .suited li::before{top:4px;width:15px;height:15px;left:2px}
  .contact{position:absolute;right:50px;top:286px;text-align:right;color:var(--white);font-style:normal}
  .contact h4{font-size:26px;font-weight:400;line-height:1.2}
  .contact .email{font-size:21px;font-weight:600;margin-top:6px;letter-spacing:.3px}
  .contact .person{font-size:17px;font-weight:600;margin-top:12px}
  .contact .line{font-size:15px;line-height:22px}
  .back .call{position:absolute;left:426px;top:400px;font-size:32px;color:var(--white);white-space:nowrap}
</style>
</head>
<body>

<section class="side front">
  <div class="hero-photo" role="img" aria-label="Photo of a woman in white on a sunny beach, holding a flowing white scarf above her head"></div>
  <p class="call">Call: <strong>604-555-0187</strong></p>

  <header class="identity">
    <h1 class="name">Maren Holloway</h1>
    <p class="creds">MA, MEd, Registered Clinical Counsellor</p>
  </header>

  <p class="motto">Making Life More Meaningful (motto)</p>

  <div class="about">
    <p>Maren Holloway is a Registered Clinical Counsellor with over 16 years of experience helping people find meaning and transformation in life’s most difficult circumstances.</p>
    <p>She uses cutting edge psychotherapeutic approaches, along with warmth, compassion and humour. Her specialty training in somatic approaches to healing is particularly useful for people with chronic health problems, recovering from accidents, or seeking better awareness of the connection between their minds and their bodies.</p>
  </div>

  <div class="session-photo" role="img" aria-label="Photo of a counsellor comforting a distressed client on a sofa"></div>

  <div class="info-box qualifications">
    <h3>Qualifications:</h3>
    <ul>
      <li>MA Health Promotion</li>
      <li>MEd Counselling Psychology</li>
      <li>MA Flowfield Awareness Method and Conflict Facilitation</li>
      <li>Level 1 Somatic Resonance Therapy</li>
    </ul>
  </div>
</section>

<section class="side back">
  <svg class="wave" width="969" height="456" viewBox="0 0 969 456" aria-hidden="true">
    <path d="M0 383 C160 432 320 405 520 318 C700 242 850 244 969 258 L969 456 L0 456 Z" fill="var(--green-pale)"/>
    <path d="M255 456 C470 372 660 268 969 280 L969 456 Z" fill="var(--blue-wave)"/>
  </svg>

  <div class="testimonials">
    <h2>What Maren’s Clients Say</h2>
    <blockquote class="quote">“ Maren helped me radically shift how I relate to my body difficulties. They used to be monsters that scared me, now I see them as allies helping me bring my passion out into the world”
      <cite>– Participant in “Body Wisdom” Course</cite></blockquote>
    <blockquote class="quote">“I used to have nightmares every night. Working with Maren helped me find the power in my dreams, my history, my struggle to be who I am in the world. Now my dreams are guides telling me I’m on the right track.”
      <cite>- F. D. Business Owner, Trauma Survivor</cite></blockquote>
    <blockquote class="quote">“Working with Maren is magic!!”
      <cite>– D.B. Medical Lab Assistant</cite></blockquote>
  </div>

  <div class="info-box suited">
    <h3>Uniquely Suited for Clients who struggle with:</h3>
    <ul>
      <li>Anxiety or depression related to health concerns</li>
      <li>Trauma-related difficulties of mind, body or spirit</li>
      <li>Chronic, undiagnosed somatic complaints</li>
      <li>Nightmares</li>
      <li>Relationship conflicts</li>
    </ul>
  </div>

  <p class="call">Call: <strong>604-555-0187</strong></p>

  <address class="contact">
    <h4>Contact Us:</h4>
    <p class="email">marenholloway@inboxmail.com</p>
    <p class="person">Maren Holloway, MA, MEd</p>
    <p class="line">Counselling Psychology</p>
    <p class="line">Vancouver, BC</p>
  </address>
</section>

</body>
</html>
```